Elegant Candy Buffet & Jar Hire Needs a logo & business card design

I need a logo design and a business card design for a new candy buffet company based in Melbourne called "Maple Candy Buffet & Jar Hire"(but the & Jar Hire part to be in smaller font). We set up candy bars with a wide variety of custom themes or to the customer's preference, we also hire out the glass jars if the customer prefers to do it themselves. But i want the emphasis on the front of the business card to be about the Candy Buffet and the jar hire can be at the back of the card. I would like to see designs that use the tiffany blue, or black and gold. I would like to see elegance, class but quite simple.

Industry/Entity Type

Business

Font styles to use
Script

```html
<!DOCTYPE html>
<html lang="en">
<head>
<meta charset="utf-8">
<title>Maple Candy Buffet &amp; Jar Hire – Business Card</title>
<link rel="stylesheet" href="https://fonts.googleapis.com/css2?family=Great+Vibes&family=Montserrat:wght@300;400&display=swap">
<style>
  :root {
    --tiffany: #6cc8c6;
    --tiffany-soft: #a9dedb;
    --mint-wash: #dcefec;
    --cream: #fcf9f4;
    --grey: #b3b3b3;
  }
  html, body {
    margin: 0;
    padding: 0;
    overflow: hidden;
  }
  body {
    width: 686px;
    height: 1200px;
    background: var(--cream);
  }
  .card {
    position: relative;
    width: 686px;
    height: 1200px;
    overflow: hidden;
  }
  .stripe-border {
    position: absolute;
    inset: 0;
    background: linear-gradient(135deg, var(--mint-wash), #e8f5f3 50%, var(--mint-wash));
  }
  .panel {
    position: absolute;
    left: 32px;
    top: 29px;
    width: 625px;
    height: 1139px;
    background: var(--cream);
  }
  .brand {
    position: absolute;
    left: 0;
    right: 0;
    top: 120px;
    text-align: center;
    font-family: "Montserrat", sans-serif;
    font-weight: 300;
    color: var(--tiffany);
    letter-spacing: 0.02em;
  }
  .brand-dot {
    width: 40px;
    height: 40px;
    border-radius: 50%;
    background: var(--tiffany);
    margin: 0 auto 40px;
  }
  .brand-name {
    display: block;
    font-size: 150px;
    line-height: 1;
    margin-bottom: 70px;
  }
  .brand-service {
    display: block;
    font-size: 47px;
    line-height: 1.2;
  }
  .brand-amp {
    display: block;
    font-size: 30px;
    line-height: 1.5;
  }
  .tagline {
    position: absolute;
    left: 0;
    right: 0;
    top: 748px;
    text-align: center;
  }
  .tagline-lead,
  .tagline-tail,
  .contact-phone {
    font-family: "Montserrat", sans-serif;
    font-weight: 300;
    color: var(--grey);
    font-size: 35px;
    line-height: 1;
    margin: 0;
  }
  .tagline-feature {
    font-family: "Great Vibes", cursive;
    color: var(--tiffany);
    font-size: 74px;
    line-height: 1;
    margin: 22px 0 14px;
  }
  .divider-scroll {
    position: absolute;
    left: 298px;
    top: 982px;
    width: 90px;
    height: 18px;
    border-radius: 9px;
    background: linear-gradient(90deg, transparent, var(--tiffany) 50%, transparent);
  }
  .contact {
    position: absolute;
    left: 0;
    right: 0;
    top: 1020px;
    text-align: center;
  }
  .contact-name {
    font-family: "Great Vibes", cursive;
    color: var(--tiffany);
    font-size: 76px;
    line-height: 1;
    margin: 0 0 14px;
  }
</style>
</head>
<body>
  <main class="card">
    <div class="stripe-border" role="img" aria-label="Soft diagonal pastel stripe pattern framing the card"></div>
    <div class="panel"></div>

    <header class="brand">
      <div class="brand-dot"></div>
      <span class="brand-name">Maple</span>
      <span class="brand-service">CANDY BUFFET</span>
      <span class="brand-amp">&amp;</span>
      <span class="brand-service">JAR HIRE</span>
    </header>

    <section class="tagline">
      <p class="tagline-lead">enjoy some</p>
      <p class="tagline-feature">sweet decadence</p>
      <p class="tagline-tail">at your next special event!</p>
    </section>

    <div class="divider-scroll" role="img" aria-label="Small ornamental scroll divider"></div>

    <section class="contact">
      <p class="contact-name">Please contact Clara</p>
      <p class="contact-phone">0412 555 019</p>
    </section>
  </main>
</body>
</html>
```